Ember Ridge Lodge website (design only)

Ember Ridg Lodge (http://www.emberridgemw.com) is a private Safari lodge located in Malawi.
We would like a modern, professional website designed that does not subscribe to the cliched view of a Safari in Africa, but still maintain a wildlife/safari atmosphere.

The aim of our website is to entice people & drive them to the booking form.

Here are some examples of websites that we like. Although we would like our site to be a bit more in line with modern web design trends.

http://www.tolukora.com/
http://www.varembo.com/
http://www.pelomavuto.com/

Requirements
Must have
• Here is a list of the pages required. Most of them will follow a standard content layout. I.e. heading, body and images.

If you take a look at the website, you will get an idea of hoe many page types there are +- 5

http://www.emberridgemw.com/index.htm

About Ember Ridge
Kotelo Country Club
Rooms
Conferences
Cuisine
Facilities
Your Safari
Activities
Rates & Special Offers
Booking form
Latest Developments
How To Get There
Gallery
Contact Us
Blog / Newsfeed

```html
<!DOCTYPE html>
<html lang="en">
<head>
<meta charset="utf-8">
<title>Ember Ridge Lodge</title>
<link href="https://fonts.googleapis.com/css2?family=Oswald:wght@400;500&family=Roboto+Condensed:wght@400;700&family=Open+Sans:ital,wght@0,400;0,600;1,400&display=swap" rel="stylesheet">
<style>
:root{
  --green:#5f9a1c;
  --green-btn:#6aa51f;
  --dark:#2e2e2e;
  --text:#333;
  --band:#ececec;
  --red:#c0272d;
  --white:#fff;
  --footer-head:#d8d8d8;
}
*{box-sizing:border-box;margin:0;padding:0}
html,body{width:727px;height:1200px;overflow:hidden;background:var(--white)}
body{position:relative;font-family:"Open Sans",Arial,sans-serif;color:var(--text)}
.abs{position:absolute}

/* header */
.brand{left:26px;top:22px;font-family:"Oswald",sans-serif;font-size:41px;color:var(--green);letter-spacing:.5px;line-height:1}
.estate{left:150px;top:73px;font-family:"Roboto Condensed",sans-serif;font-weight:700;font-size:12px;color:#333;letter-spacing:.3px}
.phone{left:546px;top:14px;display:flex;align-items:center;gap:2px;font-family:"Roboto Condensed",sans-serif;font-size:18px;color:#333;white-space:nowrap}
.search{left:553px;top:62px;width:157px;height:22px;border:1px solid #ccc;display:flex;align-items:center;justify-content:space-between;padding-left:6px;font-size:9px;font-style:italic;color:#999}
.search-btn{width:22px;height:20px;border-left:1px solid #ccc;display:flex;align-items:center;justify-content:center;background:#f4f4f4}

/* nav */
.nav{left:0;top:94px;width:727px;height:36px;background:var(--dark);display:flex;font-family:"Roboto Condensed",sans-serif;font-size:11.2px;color:#fff}
.nav span{flex:1 1 auto;display:flex;align-items:center;justify-content:center;border-right:1px solid #555;white-space:nowrap;padding:0 4px}
.nav span:last-child{border-right:0}
.nav .active{color:var(--green);background:#3a3a3a}

/* hero */
.hero{left:16px;top:145px;width:508px;height:300px;background:linear-gradient(180deg,#9db2c4 0%,#b7c6cf 25%,#4d6a3a 55%,#5f8a3a 80%,#6d8f3e 100%)}
.hero-cap{right:10px;bottom:12px;font-family:"Oswald",sans-serif;font-size:14px;color:#fff;letter-spacing:.3px}
.thumbs{left:16px;top:454px;width:508px;display:flex;justify-content:space-between}
.thumb{width:94px;height:63px;border:3px solid #fff;outline:1px solid #ddd}

/* booking */
.booking{left:533px;top:145px;width:191px;height:375px;border:1px solid #bbb;padding:0 7px}
.booking h2{font-family:"Oswald",sans-serif;font-weight:400;font-size:13px;text-align:center;height:30px;line-height:30px;border-bottom:1px solid #bbb;margin:0 -7px 6px}
.lbl{font-size:8px;color:#333;margin:4px 0 2px;white-space:nowrap}
.row{display:flex;gap:6px}
.fld{height:17px;border:1px solid #aaa;font-size:7px;font-style:italic;color:#999;padding:0 4px;display:flex;align-items:center;justify-content:space-between;flex:1;white-space:nowrap;overflow:hidden}
.fld.tall{height:33px;align-items:flex-start;padding-top:3px;white-space:normal}
.fld .dd{width:12px;height:100%;border-left:1px solid #aaa;display:flex;align-items:center;justify-content:center;margin-right:-4px;flex:none}
.tri{width:0;height:0;border-left:4px solid transparent;border-right:4px solid transparent;border-top:5px solid #333}
.cal{width:12px;height:11px;background:#aaa;border-radius:1px;margin-right:-2px;flex:none}
.btn-book{display:block;margin:8px auto 0;width:70px;height:22px;border-radius:11px;background:var(--green-btn);color:#fff;font-family:"Oswald",sans-serif;font-size:10.5px;text-align:center;line-height:22px}

/* band */
.band{left:0;top:532px;width:727px;height:264px;background:var(--band)}
.sec-title{font-family:"Oswald",sans-serif;font-size:14px;color:#333;font-weight:400}
.sec-title.on-dark{color:var(--footer-head)}
.map{left:24px;top:572px;width:300px;height:200px;background:radial-gradient(ellipse at 55% 45%,#cfcfcf 0%,#dedede 45%,#e7e7e7 100%)}
.vline{left:337px;top:552px;width:1px;height:232px;background:#ccc}
.arrows{left:656px;top:549px;display:flex;gap:5px}
.arr{width:19px;height:19px;border-radius:50%;background:#fff;border:1px solid #999;display:flex;align-items:center;justify-content:center}
.post{width:158px}
.post-img{width:158px;height:83px;border:3px solid #fff;box-shadow:0 0 2px #aaa}
.post-date{font-family:"Oswald",sans-serif;font-size:9.5px;margin:13px 0 8px;padding-bottom:8px;border-bottom:1px solid #ccc}
.post p{font-size:7.6px;line-height:1.5;color:#555}
.pill{height:17px;padding:0 10px;border-radius:9px;background:var(--dark);color:#fff;font-family:"Oswald",sans-serif;font-size:8.5px;line-height:17px;display:inline-block}

/* about */
.about{left:16px;top:820px;width:695px}
.about h2{font-family:"Oswald",sans-serif;font-weight:400;font-size:15px;margin-bottom:12px}
.about p{font-size:8.6px;line-height:1.5;font-style:italic;color:#444;margin-bottom:9px}
.about p:first-of-type{font-style:normal}

/* footer */
.footer{left:0;top:980px;width:727px;height:220px;background:var(--dark)}
.contact-box{left:14px;top:1016px;width:112px;height:84px;border-radius:9px;background:#111;color:#fff;font-family:"Roboto Condensed",sans-serif;font-size:10px;text-align:center;line-height:1.35;padding-top:6px}
.contact-box b{font-weight:700;font-size:9.6px}
.acts{left:168px;top:1023px;width:545px;display:flex;justify-content:space-between}
.act{width:130px;height:73px;border:2px solid #fff;position:relative}
.act span{position:absolute;right:6px;bottom:4px;font-family:"Oswald",sans-serif;font-size:11px;color:#fff}
.fdiv{left:0;top:1116px;width:727px;height:1px;background:#3d3d3d}
.flinks{left:140px;top:1126px;width:440px;text-align:center;font-size:8px;line-height:2.05;color:#ccc}
.fbrand{left:28px;top:1140px;font-family:"Oswald",sans-serif;font-size:18px;color:#888}
.social{left:593px;top:1140px;display:flex;gap:5px}
.social i{width:25px;height:25px;background:#8a8a8a;border-radius:3px;display:block}
</style>
</head>
<body>

<header>
  <div class="abs brand">EMBER RIDGE LODGE</div>
  <div class="abs estate">KALUNDU ESTATE - BVUMBWE</div>
  <div class="abs phone">
    <svg width="28" height="30" viewBox="0 0 30 32" aria-hidden="true">
      <path d="M6 3c3-2 6 0 7 3l-3 3c1 4 4 8 8 10l3-3c3 1 5 4 3 7-2 3-6 3-10 0C8 19 3 12 3 8c0-2 1-4 3-5z" fill="var(--red)"/>
      <path d="M12 26q6 4 14 2" stroke="#333" stroke-width="1.3" fill="none"/>
    </svg>
    <span>+265 (0) 888 420 615</span>
  </div>
  <div class="abs search">Search Here
    <div class="search-btn">
      <svg width="13" height="13" viewBox="0 0 13 13" aria-hidden="true"><circle cx="5" cy="5" r="3.8" stroke="#222" stroke-width="1.6" fill="none"/><path d="M8 8l4 4" stroke="#222" stroke-width="2"/></svg>
    </div>
  </div>
</header>

<nav class="abs nav">
  <span class="active">About Us</span><span>Kotelo Country Club</span><span>Rooms</span><span>Conferences</span><span>Cuisine</span><span>Facilities</span><span>Your Safari</span><span>Activities</span><span>Rates &amp; Special Offers</span><span>Latest Developments</span><span>Gallery</span>
</nav>

<section>
  <div class="abs hero" role="img" aria-label="Photo of brick lodge chalets with green roofs on a lawn among trees">
    <div class="abs hero-cap">WARMEST WELCOME TO THE UNIQUE MALAWI EXPERIENCE</div>
  </div>
  <div class="abs thumbs">
    <div class="thumb" role="img" aria-label="Giraffe photo" style="background:linear-gradient(#a88c5a,#7d6a3d)"></div>
    <div class="thumb" role="img" aria-label="Dining room photo" style="background:linear-gradient(#c9b8a8,#8c4a4a)"></div>
    <div class="thumb" role="img" aria-label="Lodge grounds photo" style="background:linear-gradient(#9bb0a0,#5e7d3a)"></div>
    <div class="thumb" role="img" aria-label="Chalet exterior photo" style="background:linear-gradient(#8aa7b8,#8a5a3a 60%,#5e8a3a)"></div>
    <div class="thumb" role="img" aria-label="Zebra on grassland photo" style="background:linear-gradient(#c7d26a,#8fae3a)"></div>
  </div>

  <form class="abs booking">
    <h2>BOOKING REQUEST</h2>
    <div class="row"><div style="width:47px"><div class="lbl" style="margin-top:0">Title</div><div class="fld">Mr.<span class="dd"><i class="tri"></i></span></div></div>
    <div style="flex:1"><div class="lbl" style="margin-top:0">Name</div><div class="fld">Enter your Name</div></div></div>
    <div class="lbl">Address</div><div class="fld tall">Enter your Address</div>
    <div class="lbl">Country</div><div class="fld">-----------Select Your Country-----------<span class="dd"><i class="tri"></i></span></div>
    <div class="row"><div style="flex:1"><div class="lbl">Telephone</div><div class="fld">Enter your Ph.Number</div></div><div style="flex:1"><div class="lbl">Fax</div><div class="fld">Enter your Fax Number</div></div></div>
    <div class="lbl">Email</div><div class="fld">Enter your Email Address</div>
    <div class="row"><div style="flex:1"><div class="lbl">Dates Required From</div><div class="fld">Select Date<i class="cal"></i></div></div><div style="flex:1"><div class="lbl">Dates Required To</div><div class="fld">Select Date<i class="cal"></i></div></div></div>
    <div class="row"><div style="flex:1"><div class="lbl">Number Of Rooms</div><div class="fld">-----Select-----<span class="dd"><i class="tri"></i></span></div></div><div style="flex:1"><div class="lbl">Number Of Guests</div><div class="fld">-----Select-----<span class="dd"><i class="tri"></i></span></div></div></div>
    <div class="lbl">Other Requirements</div><div class="fld tall">Please Specify if you have any other requirements.</div>
    <span class="btn-book">BOOK NOW</span>
  </form>
</section>

<section>
  <div class="abs band"></div>
  <h2 class="abs sec-title" style="left:24px;top:546px">HOW TO GET THERE</h2>
  <div class="abs map" role="img" aria-label="Map of Malawi showing the route to the lodge near Blantyre"></div>
  <div class="abs vline"></div>
  <h2 class="abs sec-title" style="left:353px;top:546px">FROM OUR BLOG</h2>
  <div class="abs arrows">
    <span class="arr"><svg width="8" height="8" viewBox="0 0 8 8" aria-hidden="true"><path d="M6 0L1 4l5 4z" fill="#333"/></svg></span>
    <span class="arr"><svg width="8" height="8" viewBox="0 0 8 8" aria-hidden="true"><path d="M2 0l5 4-5 4z" fill="#333"/></svg></span>
  </div>
  <article class="abs post" style="left:351px;top:577px">
    <div class="post-img" role="img" aria-label="Misty forest at sunrise" style="background:linear-gradient(#f1e2c0,#a89464)"></div>
    <div class="post-date">APRIL 24, 2012</div>
    <p>Lorem ipsum dolor sit amet, consectetur adipisicing elit, sed do eiusmod tempor incididunt ut labore et dolore magna aliqua. Ut enim ad minim veniam, quis nostrud exercitation ullamco laboris nisi ut aliquip ex ea commodo consequat.</p>
  </article>
  <span class="abs pill" style="left:444px;top:774px">READ MORE</span>
  <article class="abs post" style="left:534px;top:577px">
    <div class="post-img" role="img" aria-label="Zebra in golden evening light" style="background:linear-gradient(135deg,#e39a2a,#8a4a10)"></div>
    <div class="post-date">APRIL 24, 2012</div>
    <p>Lorem ipsum dolor sit amet, consectetur adipisicing elit, sed do eiusmod tempor incididunt ut labore et dolore magna aliqua. Ut enim ad minim veniam, quis nostrud exercitation ullamco laboris nisi ut aliquip ex ea commodo consequat.</p>
  </article>
  <span class="abs pill" style="left:627px;top:774px">READ MORE</span>
</section>

<section class="abs about">
  <h2>ABOUT EMBER RIDGE</h2>
  <p>&nbsp;Ember Ridge Lodge in Malawi is situated 2 kms off the Thyolo road and is only 22kms from Malawi's commercial capital Blantyre and 12 kms from its suburb of Limbe.</p>
  <p>Ember Ridge Lodge in Malawi, is a well-enclosed game sanctuary and comprises of 220 hectares of exquisite, undulating indigenous forest and grassland and is protected by an 8 km perimeter road enclosed by a 3 meter high game fence on either side of the road.</p>
  <p>Located in a colonial town, it provides with all the requirements for a world-class holiday. Both tourists as well as business travelers find a relaxing environment in its quiet and safe surroundings. Ember Ridge Lodge at Malawi has many long stretches of roads and attractive walks spread over the property. Even the flora and the fauna are arranged in keeping with the rainforest background.</p>
</section>
<span class="abs pill" style="left:645px;top:953px">READ MORE</span>

<footer>
  <div class="abs footer"></div>
  <h2 class="abs sec-title on-dark" style="left:16px;top:988px">CONTACT US</h2>
  <div class="abs contact-box"><b>EMBER RIDGE LODGE</b><br>Kalundu Estate,<br>Bvumbwe,Thyolo<br>P. O. Box 7210,<br>Limbe, Malawi.</div>
  <h2 class="abs sec-title on-dark" style="left:162px;top:988px">ACTIVITIES &amp; RECREATION INCLUDE</h2>
  <div class="abs" style="left:687px;top:993px;display:flex;gap:3px">
    <svg width="10" height="20" viewBox="0 0 10 20" aria-hidden="true"><path d="M9 0L1 10l8 10z" fill="#bbb"/></svg>
    <svg width="10" height="20" viewBox="0 0 10 20" aria-hidden="true"><path d="M1 0l8 10-8 10z" fill="#bbb"/></svg>
  </div>
  <div class="abs acts">
    <div class="act" role="img" aria-label="Bushwalking photo" style="background:linear-gradient(#b8c4c8,#8a7a4a)"><span>BUSHWALKING</span></div>
    <div class="act" role="img" aria-label="Fishing photo" style="background:linear-gradient(#8fb6d6,#2f5f8a)"><span>FISHING</span></div>
    <div class="act" role="img" aria-label="Sailing photo" style="background:linear-gradient(#5f8fbf,#1f3f6a)"><span>SAILING</span></div>
    <div class="act" role="img" aria-label="Trekking photo" style="background:linear-gradient(#6fa6d8,#e8eef4 60%,#7a7a6a)"><span>TRECKING</span></div>
  </div>
  <div class="abs fdiv"></div>
  <div class="abs flinks">About Us | Kotelo Country Club | Rooms | Conferences | Booking Request | Cuisine | Facilities<br>Your Safari | Activities | Rates &amp; Special Offers | Latest Developments | Gallery<br>2011 © www.emberridgemw.com | All rights reserved</div>
  <div class="abs fbrand">EMBER RIDGE</div>
  <div class="abs social" aria-label="Social links"><i></i><i></i><i></i><i></i></div>
</footer>

</body>
</html>
```